Geothermal company needs a creative "POW" business card

Manufacturers tend to be boring. We are not! We are a Geothermal Heat Pump company that has over 30 yrs of experience and wants a new look and updated feel. Nothing old (yawn) so get your creative hats on and let's rock!

We want to use the great colors of lime green and navy blue. Our new logo is attached and we're ready to roll. Remember, we're a professional leader in the geothermal industry that needs to make an eye catching and memorable first glance.

```html
<!DOCTYPE html>
<html lang="en">
<head>
<meta charset="utf-8">
<title>Boreal Terra – Folded Business Card</title>
<link rel="stylesheet" href="https://fonts.googleapis.com/css2?family=Source+Sans+3:wght@400;600&display=swap">
<style>
  :root {
    --lime: #8dc63f;
    --lime-pale: #c6e394;
    --navy: #2c3e5c;
    --ink: #3a3a3a;
    --paper: #ffffff;
    --backdrop: #e9ebec;
    --fold: #d9dcdd;
    --hole-shadow: rgba(0,0,0,0.25);
  }
  * { box-sizing: border-box; margin: 0; padding: 0; }
  html, body {
    width: 1200px; height: 1000px; overflow: hidden;
    background: var(--backdrop);
    font-family: "Source Sans 3", Arial, sans-serif;
  }
  .canvas { position: relative; width: 1200px; height: 1000px; }

  .card {
    position: absolute; left: 100px; width: 1000px; height: 286px;
    display: flex;
    box-shadow: 0 4px 12px rgba(0,0,0,0.25);
  }
  .card--outside { top: 170px; background: var(--lime); }
  .card--inside  { top: 544px; background: var(--paper); }

  .panel { position: relative; width: 50%; height: 100%; }
  .card--inside .panel + .panel { border-left: 1px solid var(--fold); }

  .die-cut {
    position: absolute; width: 110px; height: 110px; border-radius: 50%;
    box-shadow: inset 3px 3px 6px var(--hole-shadow);
  }
  .card--outside .die-cut { left: 58px; top: 88px; background: var(--backdrop); }
  .card--inside .die-cut  { left: 57px; top: 88px; background: var(--lime); }

  .ring-pattern {
    position: absolute; inset: 0;
    background: radial-gradient(circle at 113px 143px, var(--lime) 0 60px, var(--lime-pale) 60px, var(--lime) 78%);
    opacity: 0.55;
  }

  .web-contact {
    position: absolute; left: 0; right: 0; top: 128px;
    text-align: center; color: var(--paper);
    font-size: 16px; line-height: 1.3;
  }

  .person {
    position: absolute; right: 57px; top: 68px;
    text-align: right; color: var(--ink);
  }
  .person__name { color: var(--lime); font-weight: 600; font-size: 24px; line-height: 1.1; }
  .person__title { font-size: 20px; letter-spacing: 1px; margin-top: 4px; }
  .person__address { font-size: 15px; line-height: 1.35; margin-top: 22px; }

  .brand {
    position: absolute; left: 70px; top: 112px;
    display: flex; align-items: center; gap: 14px;
  }
  .brand__dot { width: 64px; height: 64px; border-radius: 50%; background: var(--navy); flex: none; }
  .brand__name { color: var(--lime); font-weight: 600; font-size: 44px; line-height: 1; }
  .brand__tagline { color: var(--navy); font-size: 11.5px; margin-top: 2px; }
</style>
</head>
<body>
<main class="canvas">

  <section class="card card--outside" aria-label="Outside of folded card">
    <div class="panel panel--back">
      <p class="web-contact">
        Email: jmaple@borealterra.com<br>
        www.borealterra.com
      </p>
    </div>
    <div class="panel panel--cover">
      <div class="ring-pattern" role="img" aria-label="Concentric pale green dash pattern radiating from the die-cut circle"></div>
      <div class="die-cut" aria-hidden="true"></div>
    </div>
  </section>

  <section class="card card--inside" aria-label="Inside of folded card">
    <div class="panel panel--contact">
      <div class="die-cut" aria-hidden="true"></div>
      <div class="person">
        <p class="person__name">Jon Maple</p>
        <p class="person__title">CEO</p>
        <p class="person__address">
          18 Birch Hollow Rd,<br>
          Elkton, MN 55900<br>
          Phone: (555) 014-2200<br>
          Fax: (555) 014-2201
        </p>
      </div>
    </div>
    <div class="panel panel--brand">
      <div class="brand">
        <span class="brand__dot" aria-hidden="true"></span>
        <div>
          <p class="brand__name">Boreal Terra</p>
          <p class="brand__tagline">Manufacturer of Geothermal Heat Pumps for the North</p>
        </div>
      </div>
    </div>
  </section>

</main>
</body>
</html>
```